GHollis Busisness Card

I am an aerospace consultant and at this time only need business cards.

Industry/Entity Type

Business

Contact Information for Business Card

Hollis Partners,LLC
Gerald T. Hollis

348 Birch Hollow Road
Madison AL 35762

256-555-0148 (cell)
256-555-0173 (fax)

geraldhollis@mailbrook.net

```html
<!DOCTYPE html>
<html lang="en">
<head>
<meta charset="utf-8">
<title>Hollis Partners Business Card</title>
<link href="https://fonts.googleapis.com/css2?family=Lato:wght@400;700;900&display=swap" rel="stylesheet">
<style>
  :root {
    --cyan: #1ec3d4;
    --ink: #141414;
    --card: #ffffff;
    --backdrop: #3a3a3c;
  }
  * { margin: 0; padding: 0; box-sizing: border-box; }
  html, body {
    width: 1200px; height: 900px; overflow: hidden;
    background: var(--backdrop);
    font-family: "Lato", sans-serif;
  }
  .card {
    position: absolute; left: 75px; top: 150px;
    width: 1050px; height: 600px;
    background: linear-gradient(160deg, #ffffff 0%, #f4f4f4 100%);
    box-shadow: 0 14px 40px rgba(0,0,0,0.45);
    overflow: hidden;
  }
  .band {
    position: absolute; top: 140px; height: 26px;
    background: var(--cyan);
  }
  .band--left { left: 0; width: 262px; }
  .band--right { right: 0; width: 258px; }
  .company {
    position: absolute; top: 108px; left: 262px; width: 530px;
    text-align: center;
    color: var(--cyan);
    font-weight: 900; font-size: 60px; letter-spacing: 1px;
    line-height: 1;
  }
  .person {
    position: absolute; top: 232px; left: 330px;
  }
  .person__name {
    color: var(--ink);
    font-weight: 900; font-size: 44px; letter-spacing: 0.5px;
    line-height: 1;
  }
  .person__title {
    display: inline-block; margin-top: 8px; margin-left: 36px;
    background: var(--cyan); color: #fff;
    font-weight: 700; font-size: 27px;
    padding: 2px 16px 4px; border-radius: 8px;
  }
  .contact {
    position: absolute;
    display: flex; flex-direction: column; gap: 14px;
    color: var(--ink); font-size: 27px; font-weight: 700;
  }
  .contact--right { left: 640px; top: 368px; }
  .contact--left { right: 450px; top: 440px; align-items: flex-end; }
  .contact__row { display: flex; align-items: center; gap: 12px; white-space: nowrap; }
  .contact__icon { width: 30px; height: 30px; flex: none; }
</style>
</head>
<body>
  <div class="card">
    <div class="band band--left"></div>
    <div class="band band--right"></div>
    <div class="company">HOLLIS PARTNERS</div>

    <div class="person">
      <div class="person__name">GERALD T. HOLLIS</div>
      <div class="person__title">Aerospace Consultant</div>
    </div>

    <div class="contact contact--right">
      <div class="contact__row">
        <svg class="contact__icon" viewBox="0 0 30 30" aria-label="fax">
          <rect x="8" y="3" width="14" height="8" fill="var(--cyan)"/>
          <rect x="2" y="11" width="26" height="11" rx="2" fill="var(--cyan)"/>
          <rect x="8" y="18" width="14" height="9" fill="#fff" stroke="var(--cyan)" stroke-width="2"/>
        </svg>
        <span>256-555-0173</span>
      </div>
      <div class="contact__row">
        <svg class="contact__icon" viewBox="0 0 30 30" aria-label="email">
          <rect x="2" y="6" width="26" height="18" fill="var(--cyan)"/>
          <path d="M3 7 L15 17 L27 7" fill="none" stroke="#fff" stroke-width="2"/>
          <path d="M3 23 L12 15 M27 23 L18 15" fill="none" stroke="#fff" stroke-width="1.5"/>
        </svg>
        <span>geraldhollis@mailbrook.net</span>
      </div>
    </div>

    <div class="contact contact--left">
      <div class="contact__row">
        <span>256-555-0148</span>
        <svg class="contact__icon" viewBox="0 0 30 30" aria-label="mobile phone">
          <rect x="8" y="2" width="14" height="26" rx="3" fill="none" stroke="var(--cyan)" stroke-width="2"/>
          <circle cx="15" cy="24" r="1.5" fill="var(--cyan)"/>
        </svg>
      </div>
      <div class="contact__row">
        <span>348 Birch Hollow Road Madison AL 35762</span>
        <svg class="contact__icon" viewBox="0 0 30 30" aria-label="address">
          <path d="M15 3 L28 15 H24 V27 H18 V19 H12 V27 H6 V15 H2 Z" fill="var(--cyan)"/>
        </svg>
      </div>
    </div>
  </div>
</body>
</html>
```